Banner Ad Design Project

We have a Job Search Website, www.TalvoraHire.net. We need a Banner required for the Brindle Coast Meet Karuwa 2015. It will be a vertical banner and we need it to attract Jobseekers to apply for jobs for the BC Meet. Volunteers, casual/temporary staff and full time staff. The banner will also have the current BC Meet 2015 Karuwa logo on it. Something like the "The countdown has now begun, be apart of history, be apart of BCM 2015"

Industry/Entity Type

Games

```html
<!DOCTYPE html>
<html lang="en">
<head>
<meta charset="utf-8">
<title>BCM 2015 Countdown Banner</title>
<link href="https://fonts.googleapis.com/css2?family=Comfortaa:wght@300;700&family=Raleway:wght@200;300&display=swap" rel="stylesheet">
<style>
  :root {
    --night: #02050c;
    --deep-blue: #06163a;
    --glow-blue: #1e6fd6;
    --bright-blue: #6fc3ff;
    --glow-white: #f2f9ff;
    --ink: #0b0d12;
    --paper: #ffffff;
    --muted: #4a4f5a;
    --mark-grey: #5b6068;
  }
  html, body {
    margin: 0;
    padding: 0;
    width: 800px;
    height: 1200px;
    overflow: hidden;
    background: var(--night);
  }
  .banner {
    position: relative;
    width: 800px;
    height: 1200px;
    overflow: hidden;
    background: var(--night);
    font-family: "Comfortaa", sans-serif;
  }
  .light-band-top {
    position: absolute;
    left: 0; top: 236px;
    width: 800px; height: 80px;
    background: radial-gradient(ellipse 55% 26% at 50% 50%, rgba(111,195,255,0.75), rgba(30,111,214,0.25) 55%, transparent 80%);
  }
  .light-field {
    position: absolute;
    left: 0; top: 380px;
    width: 800px; height: 660px;
    background:
      radial-gradient(circle 18px at 24% 34%, rgba(200,230,255,0.35), transparent 100%),
      radial-gradient(circle 14px at 65% 38%, rgba(200,230,255,0.45), transparent 100%),
      radial-gradient(circle 16px at 83% 40%, rgba(200,230,255,0.35), transparent 100%),
      radial-gradient(circle 22px at 47% 57%, rgba(200,230,255,0.35), transparent 100%),
      radial-gradient(circle 20px at 58% 63%, rgba(200,230,255,0.4), transparent 100%),
      radial-gradient(circle 18px at 74% 55%, rgba(200,230,255,0.3), transparent 100%),
      radial-gradient(circle 24px at 44% 78%, rgba(200,230,255,0.25), transparent 100%),
      radial-gradient(circle 14px at 10% 82%, rgba(200,230,255,0.3), transparent 100%),
      radial-gradient(circle 16px at 66% 82%, rgba(200,230,255,0.25), transparent 100%),
      radial-gradient(ellipse 30% 13% at 22% 54%, var(--glow-white) 0%, rgba(205,235,255,0.95) 40%, transparent 100%),
      radial-gradient(ellipse 48% 22% at 24% 56%, rgba(150,210,255,0.85), rgba(60,140,230,0.5) 55%, transparent 100%),
      radial-gradient(ellipse 80% 7% at 55% 52%, rgba(150,210,255,0.7), transparent 100%),
      radial-gradient(ellipse 70% 45% at 30% 50%, rgba(30,111,214,0.7), rgba(6,22,58,0.5) 60%, transparent 95%);
  }
  .headline {
    position: absolute;
    left: 0; top: 0;
    width: 800px;
    color: var(--paper);
    margin: 0;
    font-weight: 700;
  }
  .headline-the {
    position: absolute;
    left: 116px; top: 112px;
    font-size: 80px;
    font-weight: 300;
    line-height: 1;
  }
  .headline-countdown {
    position: absolute;
    left: 34px; top: 160px;
    font-size: 128px;
    font-weight: 700;
    letter-spacing: -2px;
    line-height: 1;
  }
  .headline-begun {
    position: absolute;
    left: 326px; top: 272px;
    font-size: 52px;
    font-weight: 300;
    line-height: 1;
  }
  .call {
    position: absolute;
    left: 38px;
    font-family: "Raleway", sans-serif;
    font-weight: 300;
    line-height: 1;
    margin: 0;
  }
  .call-lead-dark { top: 612px; font-size: 60px; color: var(--ink); }
  .call-history { top: 652px; font-size: 140px; color: var(--ink); letter-spacing: -1px; font-weight: 300; }
  .call-lead-light { top: 816px; font-size: 60px; color: var(--paper); }
  .call-event { top: 880px; font-size: 106px; color: var(--paper); font-weight: 200; }
  .mark-small {
    position: absolute;
    left: 22px; top: 28px;
    display: flex; align-items: center; gap: 6px;
    color: var(--mark-grey);
    font-size: 12px; font-weight: 700;
  }
  .mark-small .dot, .mark-large .dot {
    width: 10px; height: 10px; border-radius: 50%;
    background: var(--mark-grey);
  }
  .mark-large {
    position: absolute;
    right: 36px; top: 1090px;
    display: flex; align-items: center; gap: 12px;
    color: var(--mark-grey);
    font-size: 26px; font-weight: 700;
  }
  .mark-large .dot { width: 18px; height: 18px; }
  .site-url {
    position: absolute;
    left: 32px; top: 1142px;
    color: var(--muted);
    font-size: 20px;
    font-weight: 300;
  }
</style>
</head>
<body>
  <div class="banner">
    <div class="light-band-top"></div>
    <div class="light-field" role="img" aria-label="Glowing blue light streak with soft bokeh sparkles"></div>

    <div class="mark-small"><span class="dot"></span>BC Meet</div>

    <h1 class="headline">
      <span class="headline-the">The</span>
      <span class="headline-countdown">Countdown</span>
      <span class="headline-begun">has now begun,</span>
    </h1>

    <p class="call call-lead-dark">be apart of</p>
    <p class="call call-history">history,</p>
    <p class="call call-lead-light">be apart of</p>
    <p class="call call-event">BCM 2015</p>

    <div class="mark-large"><span class="dot"></span>BC Meet 2015 Karuwa</div>

    <div class="site-url">www.TalvoraHire.net</div>
  </div>
</body>
</html>
```